Composite decking sales poster

Poster advertising our brand of decking and our industry-best warranty.
Poster dimensions 1200mm wide x 400mm high.
50 Year Stain and Fade Warranty.
Ultra-Low Maintenance.
Environmentally Friendly Made from Recycled Materials.
Website: https://velmorboards.com.au
Phone: 1300 482 937
*** Uploaded pictures are optional to use ***
Must list website, phone number and logos.

```html
<!DOCTYPE html>
<html lang="en">
<head>
<meta charset="utf-8">
<title>Velmor Boards – Composite Decking Poster</title>
<link href="https://fonts.googleapis.com/css2?family=Lato:wght@400;700;900&display=swap" rel="stylesheet">
<style>
  :root {
    --stage: #8f8f8f;
    --paper: #ffffff;
    --timber-dark: #5e463c;
    --timber-mid: #86685a;
    --timber-light: #a2806f;
    --pool-deep: #145f93;
    --pool-light: #2f8fc2;
    --deck-grey: #8d8888;
    --deck-light: #a49f9d;
    --brand-ink: #454143;
    --brand-blue: #4a6f9f;
    --pill-blue: #4c6f9c;
    --white: #ffffff;
  }
  * { margin: 0; padding: 0; box-sizing: border-box; }
  html, body { width: 1200px; height: 462px; overflow: hidden; }
  body {
    background: linear-gradient(90deg, #8c8c8c, #9a9a9a);
    font-family: 'Lato', sans-serif;
    position: relative;
  }
  .poster {
    position: absolute;
    left: 91px; top: 62px;
    width: 1018px; height: 339px;
    overflow: hidden;
    background: var(--timber-mid);
  }
  .timber-photo {
    position: absolute; inset: 0;
    background: linear-gradient(135deg, var(--timber-light) 0%, var(--timber-mid) 40%, var(--timber-dark) 75%, var(--timber-mid) 100%);
  }
  .poster-shapes { position: absolute; inset: 0; }
  .deck-photo {
    position: absolute; left: 736px; top: 0; width: 282px; height: 339px;
    background: linear-gradient(180deg, var(--deck-light), var(--deck-grey));
  }
  .brand {
    position: absolute; left: 36px; top: 26px;
    display: flex; align-items: center; gap: 12px;
  }
  .brand-mark {
    width: 30px; height: 30px; background: var(--brand-blue);
  }
  .brand-name {
    font-weight: 900; font-size: 30px; letter-spacing: 0.5px;
    color: var(--brand-ink); line-height: 1;
  }
  .features { position: absolute; left: 530px; top: 78px; width: 200px; }
  .feature {
    position: absolute; left: 0; display: flex; align-items: flex-start;
  }
  .feature-icon {
    position: absolute; left: 0; width: 42px; height: 42px;
  }
  .feature-text {
    position: absolute; left: 51px; width: 160px;
    color: var(--white); font-weight: 700; font-size: 12.5px; line-height: 15.4px;
  }
  .feature-rule {
    position: absolute; left: 51px; width: 138px; height: 1px; background: rgba(255,255,255,0.85);
  }
  .contact-pill {
    position: absolute; left: 35px; top: 284px; width: 473px; height: 38px;
    border-radius: 19px; background: var(--pill-blue);
    display: flex; align-items: center; padding-left: 9px; gap: 6px;
    color: var(--white); font-weight: 700; font-size: 19px;
  }
  .contact-icon { width: 24px; height: 24px; flex: none; }
  .contact-sep { margin: 0 2px; font-weight: 400; }
</style>
</head>
<body>
  <div class="poster">
    <div class="timber-photo" role="img" aria-label="Photo of brown composite decking boards laid in a herringbone pattern"></div>

    <svg class="poster-shapes" width="1018" height="339" viewBox="0 0 1018 339">
      <defs>
        <linearGradient id="pool" x1="0" y1="0" x2="1" y2="1">
          <stop offset="0" stop-color="#0f5589"/>
          <stop offset="0.55" stop-color="#2a84b8"/>
          <stop offset="1" stop-color="#1a6ea3"/>
        </linearGradient>
        <clipPath id="leftOfDeck"><rect x="0" y="0" width="736" height="339"/></clipPath>
      </defs>
      <path class="header-band" d="M0 0 H660 C570 0 525 18 478 48 C430 78 390 86 330 86 H0 Z" fill="#ffffff"/>
      <g clip-path="url(#leftOfDeck)">
        <circle class="pool-ring" cx="735" cy="169" r="252" fill="rgba(235,225,222,0.75)"/>
        <circle class="pool-photo" cx="735" cy="169" r="243" fill="url(#pool)" role="img" aria-label="Photo of rippling blue swimming pool water"/>
      </g>
    </svg>

    <div class="deck-photo" role="img" aria-label="Photo from above of grey composite decking with a white sun lounger, laptop and coffee cup"></div>

    <div class="brand">
      <span class="brand-mark"></span>
      <span class="brand-name">VELMOR BOARDS</span>
    </div>

    <div class="features">
      <div class="feature" style="top:0">
        <svg class="feature-icon" viewBox="0 0 42 42">
          <circle cx="21" cy="21" r="20" fill="#fff" stroke="rgba(255,255,255,0.5)" stroke-width="2"/>
          <circle cx="21" cy="18" r="8" fill="none" stroke="#444" stroke-width="1.3"/>
          <path d="M21 13.5l1.4 2.9 3.1.4-2.3 2.2.6 3.1-2.8-1.5-2.8 1.5.6-3.1-2.3-2.2 3.1-.4z" fill="none" stroke="#444" stroke-width="1"/>
          <path d="M16 24l-3 7 3-1 2 2 2-6M26 24l3 7-3-1-2 2-2-6" fill="none" stroke="#444" stroke-width="1.2"/>
        </svg>
        <p class="feature-text" style="top:6px">50 Year Stain and<br>Fade Warranty.</p>
      </div>
      <div class="feature-rule" style="top:56px"></div>

      <div class="feature" style="top:68px">
        <svg class="feature-icon" viewBox="0 0 42 42">
          <circle cx="21" cy="21" r="20" fill="#fff" stroke="rgba(255,255,255,0.5)" stroke-width="2"/>
          <circle cx="22" cy="15" r="4.5" fill="none" stroke="#444" stroke-width="1.3"/>
          <circle cx="22" cy="15" r="1.6" fill="#444"/>
          <path d="M11 25h3v7h-3zM14 26h5c2 0 3 2 5 2h4c1.5 0 1.5 2 0 2h-6M14 31h8l8-4c1.5-.7 2.5 1 1 2l-8 4h-9" fill="none" stroke="#444" stroke-width="1.2"/>
        </svg>
        <p class="feature-text" style="top:6px">Ultra-Low<br>Maintenance.</p>
      </div>
      <div class="feature-rule" style="top:123px"></div>

      <div class="feature" style="top:135px">
        <svg class="feature-icon" viewBox="0 0 42 42">
          <circle cx="21" cy="21" r="20" fill="#fff" stroke="rgba(255,255,255,0.5)" stroke-width="2"/>
          <circle cx="21" cy="18" r="8" fill="none" stroke="#444" stroke-width="1.3"/>
          <path d="M21 24v-8M21 16c3-3 5-1 4 1s-4 2-4 2M21 20c-3-3-5-1-4 1s4 2 4 2" fill="none" stroke="#444" stroke-width="1.1"/>
          <path d="M16 24l-3 7 3-1 2 2 2-6M26 24l3 7-3-1-2 2-2-6" fill="none" stroke="#444" stroke-width="1.2"/>
        </svg>
        <p class="feature-text" style="top:0">Environmentally Friendly<br>Made from Recycled<br>Materials.</p>
      </div>
    </div>

    <div class="contact-pill">
      <svg class="contact-icon" viewBox="0 0 24 24">
        <circle cx="12" cy="12" r="12" fill="#fff"/>
        <path d="M8 6.5l2 2.5-1.2 1.5c.8 1.8 2 3 3.7 3.8l1.5-1.2 2.5 2-1.2 2c-4.5 0-8.5-4-8.5-8.5z" fill="var(--pill-blue)"/>
      </svg>
      <span class="contact-phone">1300 482 937</span>
      <span class="contact-sep">|</span>
      <svg class="contact-icon" viewBox="0 0 24 24">
        <circle cx="12" cy="12" r="12" fill="#fff"/>
        <g fill="none" stroke="var(--pill-blue)" stroke-width="1.2">
          <circle cx="12" cy="12" r="7"/>
          <ellipse cx="12" cy="12" rx="3" ry="7"/>
          <path d="M5 12h14M6 8.5h12M6 15.5h12"/>
        </g>
      </svg>
      <span class="contact-web">www.velmorboards.com.au</span>
    </div>
  </div>
</body>
</html>
```